Building company business card

Design and print business cards for BRENTHOLM PTY LTD.
A residantial homes building company.
Mark Lantern already designed the company Logo.

```html
<!DOCTYPE html>
<html lang="en">
<head>
<meta charset="utf-8">
<title>BRENTHOLM PTY LTD – Business Card</title>
<link rel="stylesheet" href="https://fonts.googleapis.com/css2?family=Barlow+Condensed:wght@500;600&family=Barlow+Semi+Condensed:wght@400;500&display=swap">
<style>
  :root {
    --backdrop: #2a2a2a;
    --navy: #0e1e66;
    --navy-deep: #0a1752;
    --ink: #18236b;
    --gold: #c8962f;
    --gold-light: #e0b85a;
    --paper: #f1f1f0;
    --white: #f4f4f4;
  }
  * { box-sizing: border-box; margin: 0; padding: 0; }
  html, body {
    width: 1200px; height: 1138px; overflow: hidden;
    background: var(--backdrop);
  }
  .canvas { position: relative; width: 1200px; height: 1138px; }

  .card {
    position: absolute; border-radius: 16px; overflow: hidden;
  }

  /* Front */
  .card-front {
    left: 274px; top: 186px; width: 624px; height: 376px;
    background: linear-gradient(160deg, var(--navy) 0%, var(--navy-deep) 100%);
  }
  .front-name {
    position: absolute; left: 0; right: 0; top: 150px;
    text-align: center;
    font-family: "Barlow Condensed", sans-serif; font-weight: 600;
    font-size: 56px; letter-spacing: 2px; color: var(--gold);
  }
  .front-web {
    position: absolute; left: 0; right: 0; top: 330px;
    text-align: center;
    font-family: "Barlow Semi Condensed", sans-serif; font-weight: 500;
    font-size: 16px; letter-spacing: 11px; color: #d8d8e0;
  }

  /* Back */
  .card-back {
    left: 275px; top: 608px; width: 619px; height: 374px;
    background: var(--paper);
  }
  .back-panel { position: absolute; inset: 0; width: 619px; height: 374px; }
  .back-name {
    position: absolute; left: 0; width: 282px; top: 210px;
    text-align: center;
    font-family: "Barlow Condensed", sans-serif; font-weight: 600;
    font-size: 44px; color: var(--white);
  }
  .details {
    position: absolute; left: 321px; top: 78px;
    color: var(--ink);
    font-family: "Barlow Semi Condensed", sans-serif;
  }
  .company {
    font-family: "Barlow Condensed", sans-serif; font-weight: 600;
    font-size: 38px; line-height: 1; letter-spacing: 0.5px;
  }
  .person {
    margin-top: 16px;
    font-family: "Barlow Condensed", sans-serif; font-weight: 600;
    font-size: 25px; line-height: 1;
  }
  .role { font-size: 15px; line-height: 1.2; margin-top: 2px; }
  .reg { font-size: 15px; font-weight: 500; margin-top: 12px; }
  .contact-list { list-style: none; margin-top: 6px; }
  .contact-list li {
    display: flex; align-items: center; height: 23px;
    font-size: 15px; font-weight: 500;
  }
  .contact-list svg { width: 14px; height: 14px; margin: 0 12px 0 0; fill: var(--gold); flex: none; }
</style>
</head>
<body>
<main class="canvas">

  <section class="card card-front" aria-label="Business card front">
    <div class="front-name">BRENTHOLM</div>
    <div class="front-web">www.brentholm-pl.com</div>
  </section>

  <section class="card card-back" aria-label="Business card back">
    <svg class="back-panel" viewBox="0 0 619 374" aria-hidden="true">
      <defs>
        <linearGradient id="goldEdge" x1="0" y1="0" x2="0" y2="1">
          <stop offset="0" stop-color="#b9862a"/>
          <stop offset="0.5" stop-color="#e0b85a"/>
          <stop offset="1" stop-color="#b9862a"/>
        </linearGradient>
        <linearGradient id="navyFill" x1="0" y1="0" x2="1" y2="1">
          <stop offset="0" stop-color="#0e1e66"/>
          <stop offset="1" stop-color="#0a1752"/>
        </linearGradient>
      </defs>
      <path d="M0 0 H250 Q346 181 263 374 H0 Z" fill="url(#goldEdge)"/>
      <path d="M0 0 H228 Q337 181 254 374 H0 Z" fill="url(#navyFill)"/>
    </svg>

    <div class="back-name">BRENTHOLM</div>

    <div class="details">
      <h1 class="company">BRENTHOLM PTY LTD</h1>
      <p class="person">DORIAN (DOR) HALLETT</p>
      <p class="role">Director</p>
      <p class="reg">ABN-48 210 935 602 &nbsp;|&nbsp; CDB-U 51846</p>
      <ul class="contact-list">
        <li><svg viewBox="0 0 16 16"><path d="M1 3h14v10H1z M2 4l6 5 6-5" fill="none" stroke="#c8962f" stroke-width="1.6"/></svg>dor@brentholm-pl.com</li>
        <li><svg viewBox="0 0 16 16"><path d="M2 5c0-2 3-3 6-3s6 1 6 3v1h-3V5H5v1H2z M4 7h8l2 6H2z"/></svg>0412 555 318 &amp; 0438 555 704</li>
        <li><svg viewBox="0 0 16 16"><path d="M8 1a5 5 0 0 1 5 5c0 4-5 9-5 9S3 10 3 6a5 5 0 0 1 5-5zm0 3a2 2 0 1 0 0 4 2 2 0 0 0 0-4z"/></svg>PO Box 482, Elmwood North, VIC 3109</li>
      </ul>
    </div>
  </section>

</main>
</body>
</html>
```